Looking for a professional, clean and crisp business card

I am in the underground utilities industry and am just looking for a really impressive business card. I would like our card to be white with our symbol crisp and clear with it protruding. I also have a business partner that will require his name and info on the card once the design is set. I would like to have our website info on the card which is;
http://harbortrenchco.example/

Contact Information for Business Card

Website, contact name, number and email

```html
<!DOCTYPE html>
<html lang="en">
<head>
<meta charset="utf-8">
<title>Harbor Trench Co — Business Card</title>
<link rel="stylesheet" href="https://fonts.googleapis.com/css2?family=Oswald:wght@500;600&family=Poppins:wght@400&display=swap">
<style>
  :root {
    --stage: #1c1c1e;
    --card-white: #ffffff;
    --card-dark: #0d0f12;
    --pattern-light: #1e232a;
    --ink: #2a2e36;
    --accent-blue: #3d63b8;
    --logo-white: #ffffff;
  }
  * { box-sizing: border-box; margin: 0; padding: 0; }
  html, body {
    width: 1200px;
    height: 900px;
    overflow: hidden;
    background: var(--stage);
  }
  .stage {
    position: relative;
    width: 1200px;
    height: 900px;
  }
  .card {
    position: absolute;
    left: 270px;
    width: 660px;
    height: 377px;
    overflow: hidden;
    box-shadow: 0 12px 30px rgba(0,0,0,0.55);
  }
  .card--back {
    top: 48px;
    background: var(--card-dark);
  }
  .card--front {
    top: 475px;
    background: var(--card-white);
  }
  .back-pattern {
    position: absolute;
    inset: 0;
    background: linear-gradient(135deg, var(--pattern-light) 0%, var(--card-dark) 55%, #171b21 100%);
  }
  .brand {
    position: absolute;
    display: flex;
    align-items: center;
    gap: 12px;
    font-family: "Oswald", sans-serif;
    font-weight: 600;
    font-size: 30px;
    letter-spacing: 1px;
    text-transform: uppercase;
    line-height: 1;
    white-space: nowrap;
  }
  .brand__dot {
    width: 22px;
    height: 22px;
    border-radius: 50%;
    flex: none;
  }
  .card--back .brand {
    right: 40px;
    top: 170px;
    color: var(--logo-white);
  }
  .card--back .brand__dot { background: var(--logo-white); }
  .card--front .brand {
    right: 40px;
    top: 100px;
    color: var(--ink);
  }
  .card--front .brand__dot { background: var(--ink); }
  .holder-name {
    position: absolute;
    left: 60px;
    top: 150px;
    font-family: "Oswald", sans-serif;
    font-weight: 600;
    font-size: 32px;
    letter-spacing: 1.5px;
    color: var(--ink);
    text-transform: uppercase;
  }
  .divider {
    position: absolute;
    left: 50px;
    right: 40px;
    top: 205px;
    height: 2px;
    background: var(--accent-blue);
  }
  .contact-list {
    position: absolute;
    left: 50px;
    top: 222px;
    list-style: none;
    font-family: "Poppins", sans-serif;
    font-size: 19px;
    color: var(--ink);
  }
  .contact-list li {
    display: flex;
    align-items: center;
    gap: 12px;
    height: 30px;
  }
  .contact-list svg {
    width: 20px;
    height: 20px;
    flex: none;
  }
  .contact-list .site-name { color: var(--accent-blue); }
</style>
</head>
<body>
<main class="stage">
  <section class="card card--back" aria-label="Card back">
    <div class="back-pattern" role="img" aria-label="Dark diagonal pattern of pipe sections"></div>
    <div class="brand"><span class="brand__dot"></span>Harbor Trench Co</div>
  </section>

  <section class="card card--front" aria-label="Card front">
    <div class="brand"><span class="brand__dot"></span>Harbor Trench Co</div>
    <h1 class="holder-name">Dale Morrow</h1>
    <div class="divider"></div>
    <ul class="contact-list">
      <li>
        <svg viewBox="0 0 24 24" fill="none" stroke="var(--accent-blue)" stroke-width="1.8" aria-hidden="true">
          <circle cx="12" cy="12" r="10"/>
          <path d="M8.5 7.5c.5-.5 1.3-.4 1.6.2l.8 1.6c.2.4.1.9-.2 1.2l-.6.6c.6 1.3 1.6 2.3 2.9 2.9l.6-.6c.3-.3.8-.4 1.2-.2l1.6.8c.6.3.7 1.1.2 1.6l-.8.8c-.8.8-2.1.9-3.1.3-2.1-1.2-3.8-2.9-5-5-.6-1-.5-2.3.3-3.1z"/>
        </svg>
        <span>555-014-2287</span>
      </li>
      <li>
        <svg viewBox="0 0 24 24" fill="none" stroke="var(--accent-blue)" stroke-width="1.8" aria-hidden="true">
          <rect x="2.5" y="5" width="19" height="14"/>
          <path d="M2.5 5l9.5 8 9.5-8M2.5 19l7-6.5M21.5 19l-7-6.5"/>
        </svg>
        <span>Dale@harbortrenchco.example</span>
      </li>
      <li>
        <svg viewBox="0 0 24 24" fill="none" stroke="var(--accent-blue)" stroke-width="1.8" aria-hidden="true">
          <circle cx="12" cy="12" r="10"/>
          <ellipse cx="12" cy="12" rx="4.5" ry="10"/>
          <path d="M2 12h20M4 7h16M4 17h16"/>
        </svg>
        <span>www.<span class="site-name">harbortrenchco</span>.example</span>
      </li>
    </ul>
  </section>
</main>
</body>
</html>
```